valtheon construction

i want a construction website something that really epic and eye catchy

we do full Renovation Restoration Construction

if anyone can make my jaw drop there well be a big Reward ,

i have attach my logo

Industry/Entity Type

Construction

Number of Pages Required

4 page

```html
<!DOCTYPE html>
<html lang="en">
<head>
<meta charset="utf-8">
<title>Valtheon Construction</title>
<link href="https://fonts.googleapis.com/css2?family=Open+Sans:wght@400;600;700&family=Raleway:wght@300;400&display=swap" rel="stylesheet">
<style>
:root{
  --red:#b3141b;
  --red-dark:#8c0b10;
  --ink:#333;
  --muted:#555;
  --page:#ececec;
  --rule:#d6d6d6;
}
*{box-sizing:border-box;margin:0;padding:0}
html,body{width:732px;height:1200px;overflow:hidden}
body{background:var(--page);font-family:"Open Sans",Arial,sans-serif;color:var(--ink)}
.site{position:absolute;left:22px;top:0;width:688px;height:1200px;background:#fff}
.header{height:102px;position:relative}
.brand{position:absolute;left:12px;top:30px;display:flex;align-items:center;gap:10px}
.brand-mark{width:44px;height:44px;border-radius:50%;background:var(--red)}
.brand-name{font-weight:700;color:var(--red);font-size:15px;line-height:1.1;text-transform:uppercase;letter-spacing:.3px;white-space:nowrap}
.contact-top{position:absolute;top:52px;display:flex;align-items:center;gap:8px;font-size:14px;color:var(--ink);white-space:nowrap}
.contact-top.phone{left:272px}
.contact-top.mail{left:420px}
.contact-top svg{width:18px;height:18px;fill:var(--red)}
.vsep{position:absolute;left:402px;top:44px;width:1px;height:34px;background:var(--rule)}
.nav{height:40px;background:var(--red);display:flex;align-items:center;padding-left:10px}
.nav a{color:#fff;text-decoration:none;font-size:13px;text-transform:uppercase;padding:0 18px;height:40px;line-height:40px}
.nav a.active{background:var(--red-dark)}
.hero{margin:10px 10px 0;height:292px;background:linear-gradient(160deg,#d9dcde 0%,#a9aeb2 45%,#6e6c6c 75%,#8a857f 100%)}
.dots{display:flex;justify-content:center;gap:8px;margin-top:12px}
.dots span{width:9px;height:9px;border-radius:50%;background:#555}
.dots span.on{background:var(--red)}
.section-title{display:flex;align-items:center;justify-content:center;gap:14px;margin-top:28px;font-family:"Raleway",sans-serif;font-weight:300;font-size:32px;color:var(--red-dark)}
.section-title::before,.section-title::after{content:"";width:50px;height:1px;background:#888}
.services{display:flex;justify-content:space-between;padding:0 36px;margin-top:18px}
.service{width:186px;text-align:center}
.service-img{height:103px}
.s1{background:linear-gradient(135deg,#f3f3f3,#c62a2a 55%,#ddd)}
.s2{background:linear-gradient(135deg,#6b6a5c,#9fa79a 50%,#4e5a4e)}
.s3{background:linear-gradient(180deg,#6ea6d8,#a8cbe9 60%,#d9b34a)}
.service h3{font-family:"Raleway",sans-serif;font-weight:400;font-size:22px;color:var(--red-dark);margin-top:20px}
.service p{font-size:10px;line-height:1.45;color:var(--muted);margin-top:6px;text-align:left}
.welcome{position:relative;margin-top:32px;height:232px}
.welcome h2{position:absolute;left:10px;top:0;width:440px;white-space:nowrap;font-family:"Raleway",sans-serif;font-weight:400;font-size:20px;color:var(--red-dark)}
.emblem{position:absolute;left:22px;top:72px;width:70px;height:70px;border-radius:50%;background:var(--red)}
.welcome .intro{position:absolute;left:148px;top:42px;width:296px;font-size:10px;line-height:1.45;color:var(--muted)}
.checks{position:absolute;left:190px;top:140px;width:240px;display:grid;grid-template-columns:1fr 1fr;row-gap:5px;list-style:none;font-size:10px;color:var(--muted)}
.checks li{display:flex;align-items:center;gap:6px}
.checks svg{width:12px;height:12px}
.btn{position:absolute;background:var(--red);color:#fff;font-size:11px;text-transform:uppercase;border:0;text-align:center}
.read-more{left:352px;top:204px;width:82px;height:22px;line-height:22px}
.quote{position:absolute;left:466px;top:-6px;width:212px;height:232px;border:1px solid var(--rule)}
.quote-head{background:var(--red);color:#fff;text-align:center;padding:6px 0 5px;text-transform:uppercase}
.quote-head small{display:block;font-size:10px}
.quote-head strong{display:block;font-size:17px;font-weight:600}
.field{margin:7px 12px 0;height:20px;border:1px solid var(--rule);background:#f4f4f4;font-size:9px;color:#888;padding:4px 6px}
.field.msg{height:50px}
.submit{left:50px;top:198px;width:80px;height:20px;line-height:20px}
.footer{position:absolute;left:0;top:1012px;width:688px;height:188px;background:var(--red);color:#fff}
.fnav{display:flex;align-items:center;gap:20px;position:absolute;left:10px;top:22px;font-size:11px}
.fnav a{color:#fff;text-decoration:none}
.fnav a.active{border:1px solid #fff;border-radius:14px;padding:4px 14px}
.social{position:absolute;right:14px;top:26px;display:flex;gap:26px}
.social span{width:14px;height:14px;border-radius:2px;background:#fff;opacity:.9}
.frule{position:absolute;left:10px;right:10px;top:66px;height:1px;background:rgba(255,255,255,.5)}
.fcontact{position:absolute;left:14px;top:80px}
.fcontact h4{font-weight:400;font-size:15px;margin-left:32px}
.fcol{position:absolute;top:112px;display:flex;align-items:center;gap:6px;font-size:9px;line-height:1.35}
.fcol i{width:22px;height:22px;border-radius:50%;background:#fff;flex:none}
.copy{position:absolute;right:14px;top:120px;font-size:9px}
</style>
</head>
<body>
<div class="site">
  <header class="header">
    <div class="brand"><span class="brand-mark"></span><span class="brand-name">Valtheon<br>Construction Co.</span></div>
    <div class="contact-top phone"><svg viewBox="0 0 24 24"><path d="M6.6 10.8a15.1 15.1 0 0 0 6.6 6.6l2.2-2.2a1 1 0 0 1 1-.25 11.4 11.4 0 0 0 3.6.57 1 1 0 0 1 1 1V20a1 1 0 0 1-1 1A17 17 0 0 1 3 4a1 1 0 0 1 1-1h3.5a1 1 0 0 1 1 1c0 1.25.2 2.450.57 3.57a1 1 0 0 1-.25 1z"/></svg>123 456 7890</div>
    <div class="vsep"></div>
    <div class="contact-top mail"><svg viewBox="0 0 24 24"><path d="M3 5h18v14H3zM4.5 6.5v.4L12 12l7.5-5.1v-.4zM4.5 8.7V17.5h15V8.7L12 13.8z"/></svg>info@valtheonconstruction.com</div>
  </header>
  <nav class="nav"><a class="active">Home</a><a>About</a><a>Management</a><a>Project</a><a>Client</a><a>Contact</a></nav>
  <div class="hero" role="img" aria-label="Photo of a bright modern living room with white sofa and large windows"></div>
  <div class="dots"><span class="on"></span><span></span><span></span><span></span></div>

  <h2 class="section-title">Our Services</h2>
  <div class="services">
    <div class="service"><div class="service-img s1" role="img" aria-label="Photo of a worker in red overalls renovating"></div><h3>Renovation</h3><p>Lorem ipsum is simply dummy text of the printing and typesetting industry. Lorem Ipsum has been the industry.</p></div>
    <div class="service"><div class="service-img s2" role="img" aria-label="Photo of a worker restoring a building"></div><h3>Restoration</h3><p>Lorem ipsum is simply dummy text of the printing and typesetting industry. Lorem Ipsum has been the industry.</p></div>
    <div class="service"><div class="service-img s3" role="img" aria-label="Photo of cranes over a construction site"></div><h3>Construction</h3><p>Lorem ipsum is simply dummy text of the printing and typesetting industry. Lorem Ipsum has been the industry.</p></div>
  </div>

  <section class="welcome">
    <h2>Welcome to VALTHEON CONSTRUCTION CO.</h2>
    <div class="emblem"></div>
    <p class="intro">Lorem ipsum is simply dummy text of the printing and typesetting industry. Lorem Ipsum has been the industry's standard dummy text ever since the 1500s, when an unknown printer took a galley of type and scrambled it to make a type specimen book. It has survived not only five centuries.</p>
    <ul class="checks">
      <li><svg viewBox="0 0 12 12"><rect width="12" height="12" fill="#b3141b"/><path d="M2.5 6l2.3 2.3L9.5 3.5" stroke="#fff" stroke-width="1.6" fill="none"/></svg>Lorem Ipsum</li>
      <li><svg viewBox="0 0 12 12"><rect width="12" height="12" fill="#b3141b"/><path d="M2.5 6l2.3 2.3L9.5 3.5" stroke="#fff" stroke-width="1.6" fill="none"/></svg>Lorem Ipsum</li>
      <li><svg viewBox="0 0 12 12"><rect width="12" height="12" fill="#b3141b"/><path d="M2.5 6l2.3 2.3L9.5 3.5" stroke="#fff" stroke-width="1.6" fill="none"/></svg>Lorem Ipsum</li>
      <li><svg viewBox="0 0 12 12"><rect width="12" height="12" fill="#b3141b"/><path d="M2.5 6l2.3 2.3L9.5 3.5" stroke="#fff" stroke-width="1.6" fill="none"/></svg>Lorem Ipsum</li>
      <li><svg viewBox="0 0 12 12"><rect width="12" height="12" fill="#b3141b"/><path d="M2.5 6l2.3 2.3L9.5 3.5" stroke="#fff" stroke-width="1.6" fill="none"/></svg>Lorem Ipsum</li>
      <li><svg viewBox="0 0 12 12"><rect width="12" height="12" fill="#b3141b"/><path d="M2.5 6l2.3 2.3L9.5 3.5" stroke="#fff" stroke-width="1.6" fill="none"/></svg>Lorem Ipsum</li>
    </ul>
    <div class="btn read-more">Read More</div>
    <aside class="quote">
      <div class="quote-head"><small>Call us now for a</small><strong>Free Quote</strong></div>
      <div class="field">Enter Name</div>
      <div class="field">Enter Email</div>
      <div class="field">Enter Contact No</div>
      <div class="field msg">Enter Message</div>
      <div class="btn submit">Submit</div>
    </aside>
  </section>

  <footer class="footer">
    <div class="fnav"><a class="active">Home</a><a>About</a><a>Management</a><a>Project</a><a>Client</a><a>Contact</a></div>
    <div class="social"><span></span><span></span><span></span></div>
    <div class="frule"></div>
    <div class="fcontact"><h4>Contact Us</h4></div>
    <div class="fcol" style="left:14px"><i></i><span>Lorem ipsum is simply dummy<br>text of the printing and<br>typesetting industry.</span></div>
    <div class="fcol" style="left:188px"><i></i><span>Call : 123 456 789</span></div>
    <div class="fcol" style="left:302px"><i></i><span>Fax : 123 456 789</span></div>
    <div class="copy">© VALTHEON - 2015, All Rights Reserved</div>
  </footer>
</div>
</body>
</html>
```